New Summit Tile Billboard at HQ

Looking to design a catchy image / theme for a billboard located just above our corporate HQ showroom and warehouse, along the service road of a 6-lane highway. Billboard measures 8ft x 24 ft. Would like to highlight that the store location is directly beneath the sign.

We are a retail and wholesale business selling premium flooring, ready to assemble cabinets, and granite countertops. See image ideas attached. Our information:
NAME: Summit Tile, Cabinets, Countertops
ADDRESS: 417 W. Hwy 82, Duncanville, TX 75284
WEBSITE: www.summittilehub.example
PHONE: 972-8-TILEUP (972-845-3887)

```html
<!DOCTYPE html>
<html lang="en">
<head>
<meta charset="utf-8">
<title>Summit Tile Billboard</title>
<link href="https://fonts.googleapis.com/css2?family=Barlow+Condensed:wght@400;500;600;700&display=swap" rel="stylesheet">
<style>
  :root {
    --page-bg: #ececec;
    --board-white: #ffffff;
    --ink: #1d1a1b;
    --bar-dark: #231f20;
    --lime: #8cc63f;
    --wood-light: #e2ad66;
    --wood-deep: #b9783a;
    --room-warm: #c9a580;
    --room-dim: #8f6e52;
    --kitchen-cream: #e9e1d3;
    --kitchen-stone: #b9ada0;
  }
  * { margin: 0; padding: 0; box-sizing: border-box; }
  html, body {
    width: 1200px; height: 1200px; overflow: hidden;
    background: var(--page-bg);
    font-family: "Barlow Condensed", "Arial Narrow", sans-serif;
  }
  .billboard {
    position: absolute; left: 40px; top: 413px;
    width: 1120px; height: 373px;
    background: var(--board-white);
    box-shadow: 6px 10px 14px rgba(0,0,0,0.35);
    overflow: hidden;
  }
  .photo-strip { position: absolute; left: 0; top: 0; width: 1120px; height: 319px; }
  .brand {
    position: absolute; left: 156px; top: 62px; width: 470px;
    display: flex; align-items: center; justify-content: center; gap: 14px;
  }
  .brand-mark { width: 34px; height: 34px; background: var(--lime); flex: none; }
  .brand-name {
    font-weight: 700; font-size: 96px; line-height: 1; color: var(--ink);
    white-space: nowrap;
  }
  .tagline {
    position: absolute; left: 141px; top: 196px; width: 500px;
    text-align: center; font-weight: 600; font-size: 46px; line-height: 1;
    color: var(--ink); white-space: nowrap;
  }
  .here-arrow { position: absolute; left: 28px; top: 236px; width: 64px; height: 78px; }
  .services {
    position: absolute; left: 119px; top: 281px;
    display: flex; gap: 10px; align-items: baseline;
    font-size: 15.5px; font-weight: 500; color: var(--ink); white-space: nowrap;
  }
  .services-label { color: var(--lime); font-weight: 600; font-size: 18px; margin-right: 4px; }
  .contact-bar {
    position: absolute; left: 0; top: 319px; width: 1120px; height: 54px;
    background: var(--bar-dark);
    display: flex; align-items: center; justify-content: center; gap: 40px;
  }
  .contact-item {
    display: flex; align-items: center; gap: 9px;
    color: var(--lime); font-size: 22px; font-weight: 500; white-space: nowrap;
  }
  .contact-icon { width: 24px; height: 24px; flex: none; }
</style>
</head>
<body>
  <div class="billboard">
    <svg class="photo-strip" viewBox="0 0 1120 319">
      <defs>
        <linearGradient id="woodFloor" x1="0" y1="0" x2="1" y2="1">
          <stop offset="0" stop-color="var(--wood-deep)"/>
          <stop offset="1" stop-color="var(--wood-light)"/>
        </linearGradient>
        <linearGradient id="livingRoom" x1="0" y1="0" x2="1" y2="1">
          <stop offset="0" stop-color="var(--room-dim)"/>
          <stop offset="1" stop-color="var(--room-warm)"/>
        </linearGradient>
        <linearGradient id="kitchen" x1="0" y1="0" x2="1" y2="0">
          <stop offset="0" stop-color="var(--kitchen-cream)"/>
          <stop offset="1" stop-color="var(--kitchen-stone)"/>
        </linearGradient>
      </defs>
      <polygon role="img" aria-label="Photo of a room with a polished hardwood floor" points="708,0 1120,0 1120,203" fill="url(#woodFloor)"/>
      <polygon role="img" aria-label="Photo of a living room with fireplace and a granite countertop" points="703,7 1120,210 760,210" fill="url(#livingRoom)"/>
      <polygon role="img" aria-label="Photo of a kitchen with white cabinets and stone backsplash" points="764,216 1120,216 1120,319 792,319" fill="url(#kitchen)"/>
    </svg>

    <div class="brand">
      <span class="brand-mark"></span>
      <span class="brand-name">Summit Tile</span>
    </div>
    <div class="tagline">CABINETS, COUNTERPARTS</div>

    <svg class="here-arrow" viewBox="0 0 64 78">
      <path d="M22 2 H42 V46 H60 L32 76 L4 46 H22 Z" fill="none" stroke="var(--lime)" stroke-width="2.5" stroke-linejoin="round"/>
      <text x="0" y="0" transform="translate(35 8) rotate(90)" font-family="Barlow Condensed, sans-serif" font-size="9" font-weight="600" fill="var(--ink)">YOU ARE HERE</text>
    </svg>

    <div class="services">
      <span class="services-label">OUR SERVICES</span>
      <span>• SELLING PREMIUM FLOORING</span>
      <span>• READY TO ESSEMBLE CABINETS</span>
      <span>• GRANITE COUNTERTOPS</span>
    </div>

    <div class="contact-bar">
      <div class="contact-item contact-address">
        <svg class="contact-icon" viewBox="0 0 26 26"><circle cx="13" cy="13" r="13" fill="#fff"/><path d="M13 6 a5 5 0 0 1 5 5 c0 4 -5 9 -5 9 s-5 -5 -5 -9 a5 5 0 0 1 5 -5z" fill="var(--lime)"/><circle cx="13" cy="11" r="1.8" fill="#fff"/></svg>
        <span>417 W. Hwy 82, Duncanville, TX 75284</span>
      </div>
      <div class="contact-item contact-web">
        <svg class="contact-icon" viewBox="0 0 26 26"><circle cx="13" cy="13" r="13" fill="#fff"/><g fill="none" stroke="var(--lime)" stroke-width="1.6"><circle cx="13" cy="13" r="7"/><ellipse cx="13" cy="13" rx="3" ry="7"/><line x1="6" y1="13" x2="20" y2="13"/></g></svg>
        <span>WWW.SUMMITTILEHUB.EXAMPLE</span>
      </div>
      <div class="contact-item contact-phone">
        <svg class="contact-icon" viewBox="0 0 26 26"><circle cx="13" cy="13" r="13" fill="#fff"/><rect x="9" y="6" width="8" height="14" rx="1.5" fill="var(--lime)"/><rect x="10.5" y="16.5" width="5" height="1.5" fill="#fff"/></svg>
        <span>972-8-TILEUP (972 - 845 - 3887)</span>
      </div>
    </div>
  </div>
</body>
</html>
```